Quorvex - Automated robotic Inspection with AI need new business cards

We need a new design of our business cards. The company is focused on automated quality control at high speed with unmatched results. We have a logo but need a more forward leaning business card that shows that we are delivering cutting edge technology.

Contact Information for Business Card

Name
Position
Adress
Phone
Email
e.g.
Lena Holmqvist
Chief Financial Officer (CFO)

Quorvex Sweden AB
Bruksvägen 14, SE-175 43 JÄRFÄLLA, Sweden
Mobile: +46735 21 47 83 | Office: +46 8 61 94 27
www.quorvex-example.com

Font styles to use
Sans Serif

```html
<!DOCTYPE html>
<html lang="en">
<head>
<meta charset="UTF-8">
<title>Quorvex Business Card</title>
<link rel="stylesheet" href="https://fonts.googleapis.com/css2?family=Rubik:wght@300;400;500;700&display=swap">
<style>
  :root {
    --page-bg: #1b1c1f;
    --card-white: #ffffff;
    --brand-blue: #1f5288;
    --ink: #1d1f24;
    --ink-soft: #3a3d44;
    --navy-deep: #07152e;
    --navy-mid: #0c2a55;
  }
  * { margin: 0; padding: 0; box-sizing: border-box; }
  html, body {
    width: 1200px; height: 900px; overflow: hidden;
    background: var(--page-bg);
    font-family: "Rubik", Arial, sans-serif;
  }
  .sheet {
    width: 1200px; height: 900px;
    display: flex; flex-direction: column; align-items: center; justify-content: center;
    gap: 50px;
  }
  .card {
    position: relative;
    width: 650px; height: 371px;
    overflow: hidden;
    box-shadow: 0 18px 40px rgba(0,0,0,0.55);
  }

  /* Front */
  .card-front { background: var(--card-white); color: var(--ink); }
  .brand {
    position: absolute; left: 44px; top: 46px;
    display: flex; align-items: center; gap: 12px;
  }
  .brand-dot {
    width: 26px; height: 26px; border-radius: 50%;
    background: var(--brand-blue);
  }
  .brand-name {
    font-size: 44px; font-weight: 500; letter-spacing: 1px;
    color: var(--brand-blue); line-height: 1;
  }
  .contact {
    position: absolute; left: 70px; top: 140px;
    font-size: 15px; line-height: 1.3;
  }
  .person-name { font-weight: 700; font-size: 16px; text-transform: uppercase; color: var(--ink); }
  .person-role { font-weight: 300; font-size: 16px; color: var(--ink-soft); }
  .company { margin-top: 26px; font-weight: 300; color: var(--ink-soft); }
  .address { font-weight: 300; color: var(--ink-soft); }
  .lines { margin-top: 22px; list-style: none; }
  .lines li { display: flex; align-items: center; gap: 12px; font-weight: 400; color: var(--ink); }
  .lines svg { width: 13px; height: 13px; flex: none; }

  /* Back */
  .card-back { background: var(--navy-deep); }
  .back-artwork {
    position: absolute; inset: 0;
    background: radial-gradient(circle at 50% 50%, var(--navy-mid) 0%, #0a2147 38%, var(--navy-deep) 82%);
  }
  .back-brand {
    position: absolute; left: 50%; top: 50%;
    transform: translate(-50%, -50%);
    display: flex; align-items: center; gap: 16px;
  }
  .back-brand .brand-dot { width: 34px; height: 34px; background: #ffffff; }
  .back-brand .brand-name { color: #ffffff; font-size: 62px; }
</style>
</head>
<body>
<main class="sheet">

  <section class="card card-front" aria-label="Business card front">
    <div class="brand">
      <span class="brand-dot"></span>
      <span class="brand-name">Quorvex</span>
    </div>
    <div class="contact">
      <p class="person-name">Lena Holmqvist</p>
      <p class="person-role">Chief Financial Officer (CFO)</p>
      <p class="company">Quorvex Sweden AB</p>
      <p class="address">Bruksvägen 14, SE-175 43 JÄRFÄLLA, Sweden</p>
      <ul class="lines">
        <li>
          <svg viewBox="0 0 12 12" aria-hidden="true"><rect x="3" y="0.8" width="6" height="10.4" rx="1" fill="none" stroke="#1f5288" stroke-width="1.3"/></svg>
          +46735 21 47 83
        </li>
        <li>
          <svg viewBox="0 0 12 12" aria-hidden="true"><path d="M2.5 1 L4.6 1 L5.4 3.6 L4.2 4.6 C4.9 6 6 7.1 7.4 7.8 L8.4 6.6 L11 7.4 L11 9.5 C11 10.3 10.3 11 9.5 11 C5.4 11 1 6.6 1 2.5 C1 1.7 1.7 1 2.5 1 Z" fill="#1f5288"/></svg>
          +46 8 61 94 27
        </li>
        <li>
          <svg viewBox="0 0 12 12" aria-hidden="true"><circle cx="6" cy="6" r="5" fill="none" stroke="#1f5288" stroke-width="1.1"/><ellipse cx="6" cy="6" rx="2.2" ry="5" fill="none" stroke="#1f5288" stroke-width="1"/><line x1="1" y1="6" x2="11" y2="6" stroke="#1f5288" stroke-width="1"/></svg>
          www.quorvex-example.com
        </li>
      </ul>
    </div>
  </section>

  <section class="card card-back" aria-label="Business card back">
    <div class="back-artwork" role="img" aria-label="Dark navy technology artwork with circuit traces and glowing nodes"></div>
    <div class="back-brand">
      <span class="brand-dot"></span>
      <span class="brand-name">Quorvex</span>
    </div>
  </section>

</main>
</body>
</html>
```